Professional Accounting Services Flyer

Attached is a publisher document and word document each containing the flyer text. This needs to be polished and improved to become an A4 2 sided marketing flyer.
It would be helpful if the design graphics on the flyer are in keeping with the product being sold, which is accounting and financial services.
The business in essence provides outsourced Chief Financial Office (CFO) services along with bookkeeping and a range of other accounting functions.

Target Market(s)

Small to Medium sized businesses requiring accounting support beyond the traditional preparation of tax returns

Industry/Entity Type

Accounting

Colors
0255a3
3277b5
85acd3
cedeed
ffffff
000000

Requirements
Must have
• The provided text
• Professional look and feel consistent with provision of professional accounting and financial services
• 2 sided A4 flyer
Nice to have
• Effective graphics which enhance the message and are in keeping with the theme of the business
Should not have
• Tacky or gimmicky looking graphics (please keep the graphics professional looking)
• A feel that indicates that tax return preparation is part of the business

```html
<!DOCTYPE html>
<html lang="en">
<head>
<meta charset="utf-8">
<title>Meridian Advisory – Two-Sided Flyer</title>
<link rel="stylesheet" href="https://fonts.googleapis.com/css2?family=Open+Sans:wght@400;600;700&display=swap">
<style>
:root{
  --navy:#0255a3;
  --mid:#3277b5;
  --sky:#85acd3;
  --mist:#cedeed;
  --white:#ffffff;
  --ink:#000000;
  --deep:#1b3f78;
  --stage:#ebebe8;
}
*{box-sizing:border-box;margin:0;padding:0}
html,body{width:1200px;height:1200px;overflow:hidden;background:var(--stage);font-family:"Open Sans",Arial,sans-serif;color:var(--ink)}
.flyer{position:absolute;top:250px;width:618px;height:874px;transform:scale(.8);transform-origin:0 0;overflow:hidden;background:var(--mist);box-shadow:0 4px 10px rgba(0,0,0,.25)}
.flyer--front{left:58px}
.flyer--back{left:648px}
.abs{position:absolute}

/* ---------- front ---------- */
.masthead{left:0;top:0;width:618px;height:118px;background:linear-gradient(90deg,#2f6bb4,var(--navy) 45%)}
.masthead__mark{left:0;top:0;width:203px;height:158px;background:linear-gradient(135deg,var(--mist),var(--sky) 60%,var(--mid))}
.brand-dot{left:40px;top:18px;width:120px;height:120px;border-radius:50%;background:var(--white)}
.brand-name{left:236px;top:20px;font-size:60px;font-weight:700;color:var(--white);letter-spacing:2px;line-height:80px}
.brand-band{left:203px;top:118px;width:415px;height:40px;background:linear-gradient(90deg,var(--deep),var(--mid) 40%,var(--sky))}
.brand-sub{left:228px;top:118px;font-size:26px;font-weight:700;color:var(--white);letter-spacing:26px;line-height:40px}
.side{left:0;top:158px;width:203px;height:624px;background:var(--white)}
.why{left:30px;top:170px;font-size:21px;font-weight:700;color:var(--navy);line-height:22px}
.why-list{left:30px;top:274px;width:165px;list-style:none;font-size:12.4px;line-height:14.6px}
.why-list li{position:relative;padding-left:13px;margin-bottom:6px}
.why-list li::before{content:"";position:absolute;left:0;top:3px;width:9px;height:9px;border-radius:50%;background:var(--mid);box-shadow:inset 0 0 0 2px var(--sky)}
.why-close{left:36px;top:710px;width:150px;text-align:center;font-size:12.4px;font-weight:700;line-height:14.6px}
.hub{left:203px;top:158px;width:415px;height:220px}
.section-title{font-size:16px;font-weight:600;color:var(--mid);line-height:20px}
.copy{font-size:10px;line-height:11.4px;color:#111}
.copy p+p{margin-top:3px}
.tasks{left:219px;top:460px;width:386px;display:grid;grid-template-columns:repeat(4,90px);grid-auto-rows:42px;gap:6px 8px}
.task{background:var(--white);display:flex;align-items:center;justify-content:center;text-align:center;font-size:8px;font-weight:700;line-height:8.6px;color:var(--mid);text-transform:uppercase;padding:0 3px}
.lower-panel{left:203px;top:565px;width:415px;height:217px;background:linear-gradient(180deg,#c4d7ec,var(--mist))}
.footer{left:0;top:782px;width:618px;height:92px;background:linear-gradient(90deg,var(--navy),#1d62b2)}
.icon{width:16px;height:16px}

/* ---------- back ---------- */
.back-top{left:0;top:0;width:406px;height:213px;background:linear-gradient(135deg,var(--mist),#b9d0e9)}
.about{left:0;top:213px;width:406px;height:217px;background:#1f5fae}
.about .copy{color:var(--white)}
.about .section-title{color:var(--white)}
.keyman{left:0;top:430px;width:406px;height:235px;background:var(--white)}
.back-foot{left:0;top:665px;width:406px;height:209px;background:linear-gradient(180deg,var(--navy),#1d62b2)}
.back-mark{left:0;top:665px;width:140px;height:100px;background:linear-gradient(135deg,var(--mist),var(--sky) 60%,var(--mid))}
.back-dot{left:28px;top:676px;width:78px;height:78px;border-radius:50%;background:var(--white)}
.back-name{left:158px;top:680px;font-size:36px;font-weight:700;color:var(--white);letter-spacing:1px;line-height:50px}
.back-band{left:140px;top:735px;width:266px;height:30px;background:linear-gradient(90deg,var(--deep),var(--mid) 40%,var(--sky))}
.back-sub{left:165px;top:735px;font-size:16px;font-weight:700;color:var(--white);letter-spacing:16px;line-height:30px}
.faq{left:406px;top:0;width:212px;height:874px;background:#88addb}
.faq-title{left:466px;top:18px;font-size:16px;font-weight:700;color:var(--white);line-height:17px}
.faq-list{left:418px;top:72px;width:192px}
.faq-q{font-size:10.2px;font-weight:600;color:var(--white);line-height:10.8px}
.faq-a{font-size:9.6px;line-height:10.9px;color:#10213a;margin:3px 0 13px}
</style>
</head>
<body>

<!-- FRONT SIDE -->
<section class="flyer flyer--front" aria-label="Flyer front">
  <div class="abs masthead"></div>
  <div class="abs masthead__mark"></div>
  <div class="abs brand-dot"></div>
  <div class="abs brand-name">MERIDIAN</div>
  <div class="abs brand-band"></div>
  <div class="abs brand-sub">ADVISORY</div>

  <div class="abs side"></div>
  <h2 class="abs why">Why<br>Choose<br>Meridian<br>Advisory?</h2>
  <ul class="abs why-list">
    <li>Are you experiencing significant growth and facing pressure to continue to successfully manage all aspects of your business?</li>
    <li>Do you find the day to day tasks of meeting your financial, accounting and company secretarial obligations is diverting your time from your core business?</li>
    <li>Is a lack of expert financial support holding your business back from achieving its potential?</li>
    <li>Are you considering listing, raising capital, or borrowing funds to achieve your business goals?</li>
    <li>Are you looking for cost effective solutions to improve your business performance?</li>
  </ul>
  <p class="abs why-close">If this is you Meridian Advisory may be able to help you achieve these goals.</p>

  <svg class="abs hub" viewBox="203 158 415 220" aria-label="Service overview diagram">
    <g stroke="#b3cbe6" stroke-width="7">
      <line x1="411" y1="197" x2="277" y2="212"/>
      <line x1="411" y1="197" x2="544" y2="212"/>
      <line x1="411" y1="197" x2="320" y2="302"/>
      <line x1="411" y1="197" x2="502" y2="302"/>
      <line x1="411" y1="197" x2="411" y2="342"/>
    </g>
    <g fill="#5a8fc8" stroke="#a9c4e4" stroke-width="4">
      <circle cx="277" cy="212" r="42"/>
      <circle cx="544" cy="212" r="42"/>
      <circle cx="320" cy="302" r="42"/>
      <circle cx="502" cy="302" r="42"/>
      <circle cx="411" cy="342" r="42"/>
    </g>
    <circle cx="411" cy="197" r="73" fill="#1f5fae" stroke="#a9c4e4" stroke-width="4"/>
    <g fill="#fff" font-family="Open Sans, sans-serif" font-weight="700" text-anchor="middle">
      <text x="411" y="180" font-size="14">MERIDIAN</text>
      <text x="411" y="196" font-size="14">ADVISORY</text>
      <g font-size="9.5">
        <text x="411" y="213">IS FOCUSED ON</text>
        <text x="411" y="225">PROVIDING OUTSOURCED</text>
        <text x="411" y="237">SOLUTIONS TO YOUR</text>
        <text x="411" y="249">BUSINESS</text>
      </g>
      <g font-size="9">
        <text x="277" y="210">CFO</text><text x="277" y="221">SERVICES</text>
        <text x="544" y="210">BOOKKEEPING</text><text x="544" y="221">&amp; PAYROLL</text>
        <text x="320" y="294">COMPANY</text><text x="320" y="305">SECRETARIAL</text><text x="320" y="316">SERVICES</text>
        <text x="502" y="300">FORENSIC</text><text x="502" y="311">ACCOUNTING</text>
        <text x="411" y="340">FINANCIAL</text><text x="411" y="351">REPORTING</text>
      </g>
    </g>
  </svg>

  <h3 class="abs section-title" style="left:219px;top:372px">CFO Services</h3>
  <div class="abs copy" style="left:219px;top:392px;width:384px">
    <p>Large companies utilise the services of a Chief Financial Officer (CFO) to manage the financial complexity of modern businesses.</p>
    <p>CFO services allows you to have access to the same skills on a part time basis. This function allows you to have a senior financial professional assist with managing activities such as:</p>
  </div>
  <div class="abs tasks">
    <div class="task">Strategy development and execution</div>
    <div class="task">Organisational structure optimisation</div>
    <div class="task">Insurance management</div>
    <div class="task">Managing the financial team</div>
    <div class="task">Planning and budgeting</div>
    <div class="task">Debt and capital raisings</div>
    <div class="task">Negotiations with financial institutions</div>
    <div class="task">Implementation of financial systems, policies &amp; procedures</div>
  </div>

  <div class="abs lower-panel"></div>
  <h3 class="abs section-title" style="left:219px;top:572px">Company Secretarial Services</h3>
  <div class="abs copy" style="left:219px;top:592px;width:384px">
    <p>We can provide secretarial services whether your business is a private company just requiring the basics or if you operate a small capital listed entity requiring the services of a Company Secretary to meet the obligations of the corporate regulator as well as the Exchange.</p>
  </div>
  <h3 class="abs section-title" style="left:219px;top:658px">Financial Reporting</h3>
  <div class="abs copy" style="left:219px;top:678px;width:384px">
    <p>Whether you need to meet the expectations of banks or outside investors we can assist by providing the necessary skills to compile financial reports.</p>
    <p>Alternately you may need assistance meeting the tight deadlines associated with raising funds through debt and equity markets. We can provide this service along with assistance in the preparation of Prospectus documents or Information Memorandum. We are able to act as lead or provide supplemental support for an existing internal team.</p>
  </div>

  <div class="abs footer"></div>
  <svg class="abs icon" style="left:30px;top:808px" viewBox="0 0 16 16" aria-label="Phone"><circle cx="8" cy="8" r="8" fill="#fff"/><path d="M5 4.5c.5-.5 1-.5 1.3 0l.8 1.3c.2.4 0 .7-.3 1l-.3.3c.4.9 1 1.5 1.9 1.9l.3-.3c.3-.3.6-.5 1-.3l1.3.8c.5.3.5.8 0 1.3-1.5 1.5-7.5-4.5-6-6z" fill="#0255a3"/></svg>
  <svg class="abs icon" style="left:30px;top:830px" viewBox="0 0 16 16" aria-label="Email"><circle cx="8" cy="8" r="8" fill="#fff"/><rect x="4" y="5" width="8" height="6" fill="none" stroke="#0255a3" stroke-width="1.2"/><path d="M4 5l4 3.5L12 5" fill="none" stroke="#0255a3" stroke-width="1.2"/></svg>
  <svg class="abs icon" style="left:311px;top:808px" viewBox="0 0 16 16" aria-label="Fax"><circle cx="8" cy="8" r="8" fill="#fff"/><rect x="4" y="6" width="8" height="5" fill="none" stroke="#0255a3" stroke-width="1.2"/><rect x="5.5" y="3.5" width="5" height="3" fill="none" stroke="#0255a3" stroke-width="1"/></svg>
  <svg class="abs icon" style="left:311px;top:830px" viewBox="0 0 16 16" aria-label="Address"><circle cx="8" cy="8" r="8" fill="#fff"/><path d="M8 13s-3-3.4-3-5.6a3 3 0 016 0C11 9.6 8 13 8 13z" fill="#0255a3"/><circle cx="8" cy="7.3" r="1" fill="#fff"/></svg>
</section>

<!-- BACK SIDE -->
<section class="flyer flyer--back" aria-label="Flyer back">
  <div class="abs back-top"></div>
  <h3 class="abs section-title" style="left:35px;top:22px;color:var(--navy)">Forensic Accounting</h3>
  <div class="abs copy" style="left:35px;top:43px;width:362px">
    <p>Everyone hopes their employees are honest and act with integrity, however, this is not always the case. If your business has been the subject of a suspected financial crime we can help. We can conduct a forensic review and where needed provide expert testimony should the matter lead to a court case.</p>
  </div>
  <h3 class="abs section-title" style="left:35px;top:114px;color:var(--navy)">Bookkeeping and Payroll</h3>
  <div class="abs copy" style="left:35px;top:135px;width:362px">
    <p>These essential tasks form part of running every business but often take up an excessive amount of your valuable time. These tasks which are necessary can be performed by someone with the right skills allowing you to focus on the business. We can assist you with this enabling you to concentrate on the areas of your business that add the most value.</p>
  </div>

  <div class="abs about"></div>
  <h3 class="abs section-title" style="left:35px;top:233px;color:var(--white)">About Meridian Advisory</h3>
  <div class="abs copy" style="left:35px;top:254px;width:362px;color:var(--white)">
    <p>Meridian Advisory is focused on delivering services to small and medium businesses which are often only available to larger businesses. At its core Meridian Advisory is focused on providing to small and medium sized businesses the key services large organisations gain through the employment of a dedicated CFO.</p>
    <p>These services will enable you to focus your efforts on growing your business and ensuring the operations are performing to achieve the goals you have set. Meridian Advisory is able to partner with you to ensure that as the business grows, the financial and governance needs continue to keep pace and enable growth to occur efficiently and effectively.</p>
    <p>With growth and size comes complexity and Meridian Advisory is able assist you in managing these risks allowing the business to thrive and develop successfully.</p>
  </div>

  <div class="abs keyman"></div>
  <h3 class="abs section-title" style="left:35px;top:442px;color:var(--navy)">Key Management</h3>
  <div class="abs copy" style="left:35px;top:463px;width:362px">
    <p>Graham Ellison is at the heart of the business with over 25 years of experience gained across both public practice and commerce. Most of this experience has been gained working in a range of commercial organisations ranging in size from 100 staff through to organisations with over 10,000 employees. This has included senior financial positions within top 200 listed companies with operations both within Australia and operations overseas.</p>
    <p>Graham's experience extends to a range of sectors, including retailing, wholesaling, mining and exploration, construction and manufacturing. This experience is particularly extensive within fast moving consumer goods and operational mines extracting gold, copper and coal.</p>
    <p>Graham has also been involved in a range of corporate activities including business acquisitions, stock exchange listings (particularly in Singapore), debt raisings and corporate demergers. Through these activities, he has been exposed to the debt and equity market regimes in Australia, Singapore and the United States of America.</p>
  </div>

  <div class="abs back-foot"></div>
  <div class="abs back-mark"></div>
  <div class="abs back-dot"></div>
  <div class="abs back-name">MERIDIAN</div>
  <div class="abs back-band"></div>
  <div class="abs back-sub">ADVISORY</div>
  <svg class="abs icon" style="left:30px;top:779px" viewBox="0 0 16 16" aria-label="Phone"><circle cx="8" cy="8" r="8" fill="#fff"/><path d="M5 4.5c.5-.5 1-.5 1.3 0l.8 1.3c.2.4 0 .7-.3 1l-.3.3c.4.9 1 1.5 1.9 1.9l.3-.3c.3-.3.6-.5 1-.3l1.3.8c.5.3.5.8 0 1.3-1.5 1.5-7.5-4.5-6-6z" fill="#0255a3"/></svg>
  <svg class="abs icon" style="left:30px;top:801px" viewBox="0 0 16 16" aria-label="Email"><circle cx="8" cy="8" r="8" fill="#fff"/><rect x="4" y="5" width="8" height="6" fill="none" stroke="#0255a3" stroke-width="1.2"/><path d="M4 5l4 3.5L12 5" fill="none" stroke="#0255a3" stroke-width="1.2"/></svg>
  <svg class="abs icon" style="left:30px;top:822px" viewBox="0 0 16 16" aria-label="Fax"><circle cx="8" cy="8" r="8" fill="#fff"/><rect x="4" y="6" width="8" height="5" fill="none" stroke="#0255a3" stroke-width="1.2"/><rect x="5.5" y="3.5" width="5" height="3" fill="none" stroke="#0255a3" stroke-width="1"/></svg>
  <svg class="abs icon" style="left:30px;top:844px" viewBox="0 0 16 16" aria-label="Address"><circle cx="8" cy="8" r="8" fill="#fff"/><path d="M8 13s-3-3.4-3-5.6a3 3 0 016 0C11 9.6 8 13 8 13z" fill="#0255a3"/><circle cx="8" cy="7.3" r="1" fill="#fff"/></svg>

  <div class="abs faq"></div>
  <svg class="abs" style="left:416px;top:16px;width:42px;height:42px" viewBox="0 0 42 42" aria-label="Question"><circle cx="21" cy="21" r="19" fill="none" stroke="#fff" stroke-width="3"/><text x="21" y="31" text-anchor="middle" font-family="Open Sans, sans-serif" font-size="28" font-weight="600" fill="#fff">?</text></svg>
  <h2 class="abs faq-title">Frequently Asked<br>Questions</h2>
  <div class="abs faq-list">
    <p class="faq-q">If I utilise the CFO services of Meridian Advisory, does that mean I don't need to worry about the financials?</p>
    <p class="faq-a">Meridian Advisory acts as your personal CFO. Like any successful business the CEO must remain engaged with the financial health and prosperity of the business. What Meridian Advisory will do, is assist you in fully understanding this information and using financial information to drive your business forward.</p>
    <p class="faq-q">If I decide to raise capital or list my business on a stock exchange, can Meridian Advisory help me?</p>
    <p class="faq-a">Yes, there are a number of ways we can be of assistance. Meridian Advisory can act as your CFO and drive the process, including, managing the various aspects involved in raising capital and listing a company. If you already have internal resources but require additional help to achieve the outcome within the deadlines, Meridian Advisory can provide that assistance.</p>
    <p class="faq-q">Does Meridian Advisory provide taxation services?</p>
    <p class="faq-a">While Meridian Advisory does not provide taxation services, we are able to assist you through an associate who is a registered tax agent.</p>
    <p class="faq-q">Does Meridian Advisory conduct audit and assurance services?</p>
    <p class="faq-a">These services are not provided by Meridian Advisory, however there are a range of accounting firms we can direct you toward. We are also able to act in the same manner as a dedicated CFO would in engaging with these providers and managing the audit process should you require.</p>
    <p class="faq-q">Does Meridian Advisory provide expert opinions for debt and equity raisings or takeovers?</p>
    <p class="faq-a">These are specialised services which Meridian Advisory does not provide. However, we can manage the process on your behalf to achieve the outcomes required.</p>
    <p class="faq-q">Does Meridian Advisory provide Valuations?</p>
    <p class="faq-a">Meridian Advisory does not provide valuations, however, we are able to manage this process on your behalf or assist with collation of all relevant information to facilitate a valuation.</p>
  </div>
</section>

</body>
</html>
```